Finiding oppertunites in Real Estate 6.15.20

size of ad 7” x 9.6”
1-I like the ad to stand out and attract people's attention.
2-you should be able to see the text of the ad clearly .. see the attachment anything in yellow is instructions.
3-the list of topics should not be the main part of the ad
4-if you decide you want a picture or vector of a person .. (you decide)
then it should be a white male about 25-30 years old wearing a solid white or blue shirt and not long hair.
5-leave 1 inch for footer
see attachment
Good luck

Target Market(s)

potential male students 25-35 years of age

Industry/Entity Type

Education

Requirements
Must have
• will stand out and people would want to see it.
should be able to read the words of ad
Nice to have
• how to make money in real estate on one line

```html
<!DOCTYPE html>
<html lang="en">
<head>
<meta charset="utf-8">
<title>Real Estate Career Course</title>
<link rel="stylesheet" href="https://fonts.googleapis.com/css2?family=Nunito:wght@800;900&family=Roboto:wght@400;500;700;900&family=Roboto+Condensed:wght@700;800&display=swap">
<style>
  :root {
    --maroon: #430023;
    --blush: #ffd6d6;
    --magenta: #ee1590;
    --navy: #15365f;
    --ink: #1f3f63;
    --stone: #c9c9c9;
    --stone-light: #dcdcdc;
    --footer-grey: #6b6b6d;
    --white: #ffffff;
    --icon-blue: #1aa0d8;
  }
  * { margin: 0; padding: 0; box-sizing: border-box; }
  html, body { width: 875px; height: 1200px; overflow: hidden; background: var(--white); }
  .flyer {
    position: relative; width: 875px; height: 1200px; overflow: hidden;
    background: radial-gradient(ellipse at 35% 75%, #ececec 0%, var(--stone) 55%, #b9b9b9 100%);
    font-family: "Roboto", sans-serif;
  }
  .hero-photo {
    position: absolute; left: 0; top: 0; width: 875px; height: 580px;
    background: linear-gradient(115deg, #f2f2f2 0%, #b5b6ba 30%, #6a7284 55%, #2f3b52 80%, #1d2a40 100%);
  }
  .shapes { position: absolute; left: 0; top: 0; }
  .remote-tag {
    position: absolute; right: 20px; top: 26px; text-align: center;
    font-family: "Roboto", sans-serif; font-weight: 900; font-size: 47px; line-height: 40px;
    color: var(--blush);
  }
  .course-title {
    position: absolute; left: 290px; top: 238px; width: 550px; text-align: center;
    font-family: "Nunito", sans-serif; font-weight: 900; color: var(--magenta);
    font-size: 78px; line-height: 76px; letter-spacing: -0.5px;
  }
  .course-title span { display: block; }
  .headline {
    position: absolute; left: 30px; top: 574px; width: 545px; text-align: center;
    font-family: "Roboto Condensed", sans-serif; font-weight: 800; color: var(--navy);
    font-size: 61px; line-height: 64px; letter-spacing: -2px;
  }
  .audience, .promise {
    position: absolute; left: 40px; width: 525px; text-align: center;
    font-family: "Roboto", sans-serif; font-weight: 500; color: var(--ink);
    font-size: 22.5px; line-height: 27px;
  }
  .audience { top: 759px; }
  .promise { top: 840px; }
  .divider { position: absolute; left: 135px; top: 827px; width: 336px; height: 2px; background: var(--ink); }
  .session-band {
    position: absolute; left: 0; top: 942px; width: 875px; height: 118px; background: var(--maroon);
  }
  .session-count {
    position: absolute; left: 0; top: 949px; width: 604px; text-align: center;
    font-family: "Roboto", sans-serif; font-weight: 900; font-size: 46px; line-height: 52px; color: var(--blush);
  }
  .start-date {
    position: absolute; left: 0; top: 1005px; width: 604px; text-align: center;
    font-family: "Roboto", sans-serif; font-weight: 700; font-size: 30px; line-height: 36px; color: var(--white);
  }
  .topics-panel {
    position: absolute; left: 604px; top: 530px; width: 249px; height: 530px;
    background: linear-gradient(180deg, #d4d4d4, var(--stone-light) 40%, #d0d0d0);
    border-left: 1px solid #a9a9a9;
  }
  .topics-header {
    position: absolute; left: 604px; top: 643px; width: 249px; height: 64px;
    background: var(--maroon); color: var(--blush); text-align: center;
    font-family: "Roboto", sans-serif; font-weight: 700; font-size: 17px; line-height: 21px;
    padding-top: 6px;
    clip-path: polygon(0 0, 100% 0, 100% 85%, 50% 100%, 0 85%);
  }
  .topics-list {
    position: absolute; left: 619px; top: 713px; list-style: none;
    font-family: "Roboto", sans-serif; font-weight: 500; font-size: 19px; line-height: 23.7px; color: var(--ink);
  }
  .topics-list li { display: flex; align-items: center; gap: 16px; white-space: nowrap; }
  .topics-list svg { flex: none; }
  .footer-strip { position: absolute; left: 0; top: 1082px; width: 875px; height: 98px; background: var(--footer-grey); }
  .brand {
    position: absolute; left: 38px; top: 1100px; width: 270px;
    font-family: "Roboto", sans-serif; font-weight: 700; color: var(--white);
    font-size: 22px; line-height: 24px; letter-spacing: 0.3px;
  }
  .brand-note {
    position: absolute; left: 38px; top: 1148px; width: 258px; height: 18px;
    background: #8c8c8e; color: var(--white);
    font-family: "Roboto", sans-serif; font-weight: 400; font-size: 13px; line-height: 18px; text-align: center;
  }
  .contact-card {
    position: absolute; left: 318px; top: 1082px; width: 408px; height: 98px; background: var(--white);
    clip-path: polygon(14px 0, 100% 0, calc(100% - 14px) 100%, 0 100%);
  }
  .contact {
    position: absolute; font-family: "Roboto", sans-serif; font-weight: 400; font-size: 15.5px;
    color: var(--navy); display: flex; align-items: center; gap: 6px; white-space: nowrap;
  }
  .contact strong { font-weight: 700; }
  .contact-address { left: 344px; top: 1094px; }
  .contact-web { left: 341px; top: 1123px; }
  .contact-mail { left: 338px; top: 1151px; }
  .phone-icon { margin-left: 12px; }
  .classes-note {
    position: absolute; left: 726px; top: 1096px; width: 134px; text-align: center;
    font-family: "Roboto", sans-serif; font-weight: 700; font-size: 19px; line-height: 25px; color: var(--white);
  }
</style>
</head>
<body>
<main class="flyer">
  <div class="hero-photo" role="img" aria-label="Black-and-white photo of a hand placing a small model house, with a blurred red and green market chart behind it"></div>

  <svg class="shapes" width="875" height="1200" viewBox="0 0 875 1200" aria-hidden="true">
    <defs>
      <radialGradient id="stoneGlow" cx="0.35" cy="0.35" r="0.6">
        <stop offset="0" stop-color="#f2f2f2" stop-opacity="0.9"/>
        <stop offset="1" stop-color="#bdbdbd" stop-opacity="0"/>
      </radialGradient>
    </defs>
    <path d="M540 0 H875 V165 C760 175 650 140 590 80 C565 55 548 28 540 0 Z" fill="var(--maroon)"/>
    <path d="M722 168 C780 180 835 172 875 162 V186 C820 190 770 182 722 168 Z" fill="var(--maroon)"/>
    <path d="M0 580 C180 520 340 505 460 508 C640 512 780 545 875 580 V1200 H0 Z" fill="var(--stone)"/>
    <path d="M0 580 C180 520 340 505 460 508 C640 512 780 545 875 580 V1200 H0 Z" fill="url(#stoneGlow)"/>
    <path d="M0 596 C40 580 90 564 142 553 C95 572 45 592 0 612 Z" fill="var(--maroon)"/>
    <path d="M383 525 C560 518 760 540 875 605 V630 C760 565 580 535 383 525 Z" fill="var(--maroon)"/>
    <path d="M100 722 C94 710 110 705 170 700 C300 690 440 696 536 722 C420 708 260 712 120 730 C108 732 102 728 100 722 Z" fill="var(--maroon)"/>
  </svg>

  <p class="remote-tag">Remote<br>Sessions</p>

  <h1 class="course-title"><span>Real Estate</span><span>Career Course</span></h1>

  <h2 class="headline">How to Make Money<br>In Real Estate?</h2>

  <p class="audience">For those who have started<br>or would like to go into Real Estate</p>
  <div class="divider"></div>
  <p class="promise">An investment in knowledge opens up<br>untold opportunities</p>

  <div class="session-band"></div>
  <p class="session-count">12 Session Course</p>
  <p class="start-date">Classes Starting June 16</p>

  <div class="topics-panel"></div>
  <div class="topics-header">A PARTIAL<br>LISTING OF TOPICS</div>
  <ul class="topics-list">
    <li><svg width="16" height="16" viewBox="0 0 16 16"><circle cx="8" cy="8" r="6.8" fill="none" stroke="currentColor" stroke-width="1.8"/><path d="M5 8.2 L7.2 10.3 L11 6" fill="none" stroke="currentColor" stroke-width="1.8"/></svg>Single-family</li>
    <li><svg width="16" height="16" viewBox="0 0 16 16"><circle cx="8" cy="8" r="6.8" fill="none" stroke="currentColor" stroke-width="1.8"/><path d="M5 8.2 L7.2 10.3 L11 6" fill="none" stroke="currentColor" stroke-width="1.8"/></svg>Multifamily</li>
    <li><svg width="16" height="16" viewBox="0 0 16 16"><circle cx="8" cy="8" r="6.8" fill="none" stroke="currentColor" stroke-width="1.8"/><path d="M5 8.2 L7.2 10.3 L11 6" fill="none" stroke="currentColor" stroke-width="1.8"/></svg>Management</li>
    <li><svg width="16" height="16" viewBox="0 0 16 16"><circle cx="8" cy="8" r="6.8" fill="none" stroke="currentColor" stroke-width="1.8"/><path d="M5 8.2 L7.2 10.3 L11 6" fill="none" stroke="currentColor" stroke-width="1.8"/></svg>Real Estate Concepts</li>
    <li><svg width="16" height="16" viewBox="0 0 16 16"><circle cx="8" cy="8" r="6.8" fill="none" stroke="currentColor" stroke-width="1.8"/><path d="M5 8.2 L7.2 10.3 L11 6" fill="none" stroke="currentColor" stroke-width="1.8"/></svg>Real Estate law</li>
    <li><svg width="16" height="16" viewBox="0 0 16 16"><circle cx="8" cy="8" r="6.8" fill="none" stroke="currentColor" stroke-width="1.8"/><path d="M5 8.2 L7.2 10.3 L11 6" fill="none" stroke="currentColor" stroke-width="1.8"/></svg>Investment properties</li>
    <li><svg width="16" height="16" viewBox="0 0 16 16"><circle cx="8" cy="8" r="6.8" fill="none" stroke="currentColor" stroke-width="1.8"/><path d="M5 8.2 L7.2 10.3 L11 6" fill="none" stroke="currentColor" stroke-width="1.8"/></svg>Foreclosures</li>
    <li><svg width="16" height="16" viewBox="0 0 16 16"><circle cx="8" cy="8" r="6.8" fill="none" stroke="currentColor" stroke-width="1.8"/><path d="M5 8.2 L7.2 10.3 L11 6" fill="none" stroke="currentColor" stroke-width="1.8"/></svg>Rehab</li>
    <li><svg width="16" height="16" viewBox="0 0 16 16"><circle cx="8" cy="8" r="6.8" fill="none" stroke="currentColor" stroke-width="1.8"/><path d="M5 8.2 L7.2 10.3 L11 6" fill="none" stroke="currentColor" stroke-width="1.8"/></svg>Foreclosures</li>
    <li><svg width="16" height="16" viewBox="0 0 16 16"><circle cx="8" cy="8" r="6.8" fill="none" stroke="currentColor" stroke-width="1.8"/><path d="M5 8.2 L7.2 10.3 L11 6" fill="none" stroke="currentColor" stroke-width="1.8"/></svg>Short sales</li>
    <li><svg width="16" height="16" viewBox="0 0 16 16"><circle cx="8" cy="8" r="6.8" fill="none" stroke="currentColor" stroke-width="1.8"/><path d="M5 8.2 L7.2 10.3 L11 6" fill="none" stroke="currentColor" stroke-width="1.8"/></svg>Development</li>
    <li><svg width="16" height="16" viewBox="0 0 16 16"><circle cx="8" cy="8" r="6.8" fill="none" stroke="currentColor" stroke-width="1.8"/><path d="M5 8.2 L7.2 10.3 L11 6" fill="none" stroke="currentColor" stroke-width="1.8"/></svg>Finical modeling</li>
    <li><svg width="16" height="16" viewBox="0 0 16 16"><circle cx="8" cy="8" r="6.8" fill="none" stroke="currentColor" stroke-width="1.8"/><path d="M5 8.2 L7.2 10.3 L11 6" fill="none" stroke="currentColor" stroke-width="1.8"/></svg>HUD properties</li>
    <li><svg width="16" height="16" viewBox="0 0 16 16"><circle cx="8" cy="8" r="6.8" fill="none" stroke="currentColor" stroke-width="1.8"/><path d="M5 8.2 L7.2 10.3 L11 6" fill="none" stroke="currentColor" stroke-width="1.8"/></svg>Due Diligencene</li>
  </ul>

  <footer>
    <div class="footer-strip"></div>
    <p class="brand">BRIGHTPATH<br>CAREER NETWORK</p>
    <p class="brand-note">A NON-PROFIT OF COMMUNITY WORKS</p>

    <div class="contact-card"></div>
    <p class="contact contact-address">
      <svg width="20" height="20" viewBox="0 0 20 20"><circle cx="10" cy="10" r="9" fill="none" stroke="var(--icon-blue)" stroke-width="1.3"/><path d="M10 4.5 a3.6 3.6 0 0 1 3.6 3.6 c0 2.6-3.6 6.6-3.6 6.6 s-3.6-4-3.6-6.6 A3.6 3.6 0 0 1 10 4.5 Z" fill="var(--icon-blue)"/><circle cx="10" cy="8.1" r="1.3" fill="#fff"/></svg>
      <span>Northfield - Maple Ridge - Lakeport, <strong>Main Branch</strong></span>
    </p>
    <p class="contact contact-web">
      <svg width="20" height="20" viewBox="0 0 20 20"><circle cx="10" cy="10" r="9" fill="none" stroke="var(--icon-blue)" stroke-width="1.3"/><circle cx="10" cy="10" r="6" fill="none" stroke="var(--icon-blue)" stroke-width="1.2"/><path d="M4 10 H16 M10 4 V16 M5 7 H15 M5 13 H15" stroke="var(--icon-blue)" stroke-width="0.9"/></svg>
      <span>www.bpcareers.org</span>
      <svg class="phone-icon" width="22" height="22" viewBox="0 0 20 20"><circle cx="10" cy="10" r="9" fill="none" stroke="var(--icon-blue)" stroke-width="1.3"/><path d="M6.5 5.5 L8.3 5 L9.3 7.6 L8.2 8.6 C8.8 10 9.9 11.1 11.3 11.8 L12.4 10.7 L15 11.7 L14.5 13.5 C10 13.8 6.2 10 6.5 5.5 Z" fill="none" stroke="var(--icon-blue)" stroke-width="1.1"/></svg>
      <span>555 014 2200 x310</span>
    </p>
    <p class="contact contact-mail">
      <svg width="22" height="22" viewBox="0 0 20 20"><circle cx="10" cy="10" r="9" fill="none" stroke="var(--icon-blue)" stroke-width="1.3"/><rect x="5.5" y="6.8" width="9" height="6.4" rx="1" fill="var(--icon-blue)"/><path d="M5.8 7.2 L10 10.4 L14.2 7.2" fill="none" stroke="#fff" stroke-width="0.9"/></svg>
      <span>info@bpcareers.org</span>
    </p>

    <p class="classes-note">MEN'S &amp;<br>WOMEN'S<br>CLASSES</p>
  </footer>
</main>
</body>
</html>
```